Training Course Info Brochure

Hi there, I'm looking for a design for A4 Flyer (2-3 pages) on our new Course - Infection Control. I have included a previous brochure on our courses so the designed can see the look and feel we are looking for.

As this is about Infection Control, I would also like to see some RED in the design or wording.

The brochure will need to include quite a few industry/ government logos as well and graphics are important. I have included some (Health Care Industry workers) and am also open to other graphics.

Thanks for considering!

Target Market(s)

The Health profession and students wanting to work in the health field

Industry/Entity Type

Health Care

Font styles to use
Sans Serif

Colors
3277b5
f78f20
ffffff
ec1f27

Requirements
Must have
• Similar feel to the brochure I have included in this brief.

SOME RED lettering as we are teaching Infection Control during the COVID19 pandemic
Nice to have
• Lovely design with quite a few photos graphics

Company details:

Carrow Academy of Learning
RTO 73648
FREECALL : 1800 437 982
www.carrowlearning.edu.au
info@carrowlearning.edu.au

```html
<!DOCTYPE html>
<html lang="en">
<head>
<meta charset="utf-8">
<title>Infection Control Skill Set – Course Brochure</title>
<link rel="stylesheet" href="https://fonts.googleapis.com/css2?family=Source+Sans+3:wght@400;600&display=swap">
<style>
:root{
  --red:#e8262b;
  --blue:#2f73b5;
  --navy:#2b3f5c;
  --gold:#b0822a;
  --ink:#1e1e1e;
  --panel-grey:#f1f2f5;
  --white:#ffffff;
}
*{margin:0;padding:0;box-sizing:border-box}
html,body{width:1200px;height:860px;overflow:hidden;background:var(--white)}
body{font-family:"Source Sans 3",sans-serif;color:var(--ink)}
.brochure{position:relative;width:1200px;height:860px}
.panel{position:absolute;top:0;height:860px}

/* left panel */
.panel--pathways{left:0;width:406px;background:var(--panel-grey)}
.pathways__photo{position:absolute;left:0;top:0;width:406px;height:270px}
.pathways__title{position:absolute;left:43px;top:300px;font-size:23px;line-height:29px;font-weight:400;color:var(--red)}
.pathways__rule{position:absolute;left:43px;top:375px;width:214px;height:4px;background:var(--gold)}
.pathways__body{position:absolute;left:43px;top:405px;width:345px;font-size:12.6px;line-height:15.3px}
.pathways__body p+p{margin-top:15px}
.pathways__list{position:absolute;left:43px;top:537px;width:350px;list-style:none;font-size:8.7px;line-height:15.2px}
.pathways__list li{padding-left:5px;text-indent:-5px}
.pathways__list li::before{content:"• "}
.pathways__list .note{padding-left:5px}
.pathways__list .note::before{content:""}
.pathways__band{position:absolute;left:0;bottom:0;width:406px;height:45px;background:var(--gold)}
.pathways__band::before{content:"";position:absolute;left:0;top:-7px;width:406px;height:5px;background:var(--navy)}

/* middle panel */
.panel--partners{left:406px;width:387px;background:var(--white)}
.brand{display:flex;align-items:center;justify-content:center;gap:7px;font-weight:600;color:var(--navy)}
.brand__mark{width:12px;height:12px;background:var(--navy)}
.partners__brand{position:absolute;left:0;top:140px;width:387px;font-size:14px}
.partners__title{position:absolute;left:0;top:224px;width:387px;text-align:center;font-size:18px;font-weight:400;color:#333}
.partner{position:absolute;border-radius:4px}
.partners__tagline{position:absolute;left:90px;top:555px;width:185px;height:55px;border-radius:6px;background:linear-gradient(90deg,#e9d59a,#d8b655)}
.partners__foot{position:absolute;left:0;bottom:0;width:387px;height:235px}
.contact{position:absolute;left:0;top:700px;width:387px;color:var(--white)}
.contact__title{text-align:center;font-size:18.5px;font-weight:400}
.contact__rule{position:absolute;left:36px;width:316px;height:4px;background:var(--gold)}
.contact__rule--top{top:33px}
.contact__rule--bottom{top:109px}
.contact__lines{position:absolute;left:36px;top:53px;font-size:12px;line-height:17.5px}
.contact__lines span,.contact__office span{color:#d49a3c}
.contact__office{position:absolute;left:276px;top:55px;font-size:10px;line-height:10.5px}
.contact__office span{display:block;font-size:8.5px;margin-bottom:1px}

/* right panel */
.panel--cover{left:793px;width:407px;background:var(--white);text-align:center}
.cover__brand{position:absolute;left:0;top:100px;width:407px;font-size:12px}
.cover__name{position:absolute;left:0;top:151px;width:407px;font-size:19px;font-weight:400;color:var(--navy)}
.cover__title{position:absolute;left:0;top:190px;width:407px;font-size:20.5px;line-height:24.5px;font-weight:400;color:var(--red)}
.cover__unit{position:absolute;left:0;top:254px;width:407px;font-size:16.5px;line-height:20px;font-weight:400;color:var(--blue)}
.cover__photo{position:absolute;left:0;top:318px;width:407px;height:352px}
.cover__cost-title{position:absolute;left:0;top:700px;width:407px;font-size:18.5px;font-weight:400;color:var(--red)}
.cover__cost{position:absolute;left:0;top:733px;width:407px;font-size:16.5px;line-height:20px;color:var(--red)}
.cover__cost span{display:block;margin-top:6px}
</style>
</head>
<body>
<main class="brochure">

  <section class="panel panel--pathways">
    <svg class="pathways__photo" viewBox="0 0 406 270" role="img" aria-label="Photo: gloved hands forming a heart shape against a pale grey background">
      <defs>
        <linearGradient id="heartPhoto" x1="0" y1="0" x2="0" y2="1">
          <stop offset="0" stop-color="#d9dde4"/>
          <stop offset="0.6" stop-color="#9cbbe0"/>
          <stop offset="1" stop-color="#6b9ad2"/>
        </linearGradient>
      </defs>
      <path d="M0 0H406V227Q200 300 0 228Z" fill="url(#heartPhoto)"/>
      <path d="M0 228Q200 300 406 227" fill="none" stroke="var(--navy)" stroke-width="4"/>
    </svg>
    <h2 class="pathways__title">Job opportunities and<br>Study Pathways</h2>
    <div class="pathways__rule"></div>
    <div class="pathways__body">
      <p>This course does not lead to a specific job outcome but will be helpful if you are, or would like to work in any of the areas described above. Our training course is designed to make students Job Ready or to enhance their job role.</p>
      <p>The Units of Competency is a recognised Unit that can be used as a Credit Transfer in Qualifications such as :</p>
    </div>
    <ul class="pathways__list">
      <li>Certificate III Business Administration (Medical)</li>
      <li>Cert III and IV Health Administration</li>
      <li>Cert III in Individual Support (Aging, disability,<br>&nbsp;home and community)</li>
      <li>Cert III in Allied Health Assistance</li>
      <li>Cert III/IV Dental Assisting</li>
      <li>Certificate III in Aboriginal and/or Torres Strait<br>&nbsp;Islander Primary Health Care</li>
      <li>Cert II/III Community Services</li>
      <li>Certificate III in Cleaning Operations</li>
      <li>Cert II and III Health Support Services</li>
      <li class="note">More Qualifications that include this Unit of Competency can be found at<br>https://unitregister.edu.au/Details/HLTINF001</li>
    </ul>
    <div class="pathways__band"></div>
  </section>

  <section class="panel panel--partners">
    <div class="brand partners__brand"><span class="brand__mark"></span>Carrow Academy of Learning</div>
    <h2 class="partners__title">OUR PARTNERS</h2>
    <div class="partner" style="left:50px;top:295px;width:75px;height:48px;background:#e4e4e4"></div>
    <div class="partner" style="left:165px;top:280px;width:55px;height:65px;background:#f3c98e"></div>
    <div class="partner" style="left:278px;top:298px;width:55px;height:40px;background:#d6e8d6"></div>
    <div class="partner" style="left:86px;top:390px;width:210px;height:48px;background:#e8e8e8"></div>
    <div class="partner" style="left:64px;top:470px;width:130px;height:50px;background:#f6d3d3"></div>
    <div class="partner" style="left:247px;top:470px;width:82px;height:65px;background:#d3eaf3"></div>
    <div class="partners__tagline" role="img" aria-label="Hand-lettered state campaign tagline in gold"></div>
    <svg class="partners__foot" viewBox="0 0 387 235" aria-hidden="true">
      <path d="M0 10Q194 55 387 10V235H0Z" fill="var(--navy)"/>
      <path d="M0 10Q194 55 387 10" fill="none" stroke="var(--gold)" stroke-width="4"/>
    </svg>
    <div class="contact">
      <h2 class="contact__title">Contact Us</h2>
      <div class="contact__rule contact__rule--top"></div>
      <p class="contact__lines"><span>FREE CALL:</span> 1800 437 982<br><span>EMAIL:</span> info@carrowlearning.edu.au<br><span>WEB:</span> www.carrowlearning.edu.au</p>
      <p class="contact__office"><span>HEAD OFFICE:</span>PO Box 4417,<br>Riverdale DC 6090<br><br>RTO 73648</p>
      <div class="contact__rule contact__rule--bottom"></div>
    </div>
  </section>

  <section class="panel panel--cover">
    <div class="brand cover__brand"><span class="brand__mark"></span>Carrow Academy of Learning</div>
    <h1 class="cover__name">Carrow Academy of Learning</h1>
    <h2 class="cover__title">Infection Control Skill set<br>HLTSS00064 for Health Care workers</h2>
    <p class="cover__unit">HLTINF001 - Comply with infection prevention<br>and control policies and procedures</p>
    <svg class="cover__photo" viewBox="0 0 407 352" role="img" aria-label="Photo: health care worker in scrubs, goggles, mask and purple gloves">
      <defs>
        <linearGradient id="workerPhoto" x1="0" y1="0" x2="1" y2="1">
          <stop offset="0" stop-color="#5f6e8e"/>
          <stop offset="0.5" stop-color="#a9a8b4"/>
          <stop offset="1" stop-color="#6d6f7e"/>
        </linearGradient>
      </defs>
      <path d="M0 43Q203 -10 407 43V312Q203 370 0 310Z" fill="url(#workerPhoto)"/>
      <path d="M0 43Q203 -10 407 43" fill="none" stroke="var(--red)" stroke-width="5"/>
      <path d="M0 310Q203 370 407 312" fill="none" stroke="var(--red)" stroke-width="5"/>
    </svg>
    <h2 class="cover__cost-title">Course cost</h2>
    <p class="cover__cost">Free infection control skill sets for<br>everyone in Western Australia or<span>$350/for students outside of WA.</span></p>
  </section>

</main>
</body>
</html>
```